distributor of aftermarket auto electrical components

I am after business card design for my new company called
Coral Vehicle Supplies (Coral Vehicle Supplies as the acronym). I will supplying automotive wiring components, basically from battery to headlight. I will be aiming to sell in the 4wd scene and to auto electricians. i am not worried which colours are used though i would like it to be dynamic.
Updates

sorry guys, i have add a mobile and e-mail address that will need to on there as well. Sorry for theĀ inconvenience.

sorry guys i had erred on my spelling with my e-mail. i have now fixed it in the brief

Target Market(s)

4wd industry, custom cars, RV, auto electricians

Industry/Entity Type

Electrical

Requirements
Must have
• Company Name
ABN number: 47 316 208 594
Director: Morris Tandy
M 0438 271 954
E mtandyo@bellwire.com.au

```html
<!DOCTYPE html>
<html lang="en">
<head>
<meta charset="utf-8">
<title>Coral Vehicle Supplies – Business Card</title>
<link rel="stylesheet" href="https://fonts.googleapis.com/css2?family=Arimo:wght@400;700&display=swap">
<style>
  :root {
    --brand-blue: #1696c4;
    --ink: #111111;
    --paper: #ffffff;
    --ghost: #ececec;
    --stage: #ecebe8;
  }
  * { margin: 0; padding: 0; box-sizing: border-box; }
  html, body {
    width: 1200px; height: 900px; overflow: hidden;
    background: var(--stage);
    font-family: "Arimo", Arial, sans-serif;
  }
  .sheet {
    position: relative; width: 1200px; height: 900px;
    display: flex; align-items: center; justify-content: center; gap: 60px;
  }
  .card {
    position: relative; width: 500px; height: 286px; overflow: hidden;
    box-shadow: 0 6px 18px rgba(0,0,0,0.18);
  }

  /* Front */
  .card--front {
    background: var(--brand-blue);
    display: flex; align-items: center; justify-content: center;
  }
  .front-mark { display: flex; align-items: center; gap: 12px; }
  .front-mark__dot {
    flex: none; width: 22px; height: 22px; border-radius: 50%; background: var(--ink);
  }
  .front-mark__name {
    font-weight: 700; font-size: 34px; line-height: 1; color: var(--ink); white-space: nowrap;
  }

  /* Back */
  .card--back { background: var(--paper); }
  .back-ghost {
    position: absolute; right: 58px; top: 50%; transform: translateY(-50%);
    font-weight: 700; font-size: 42px; line-height: 1.05; color: var(--ghost); text-align: right;
  }
  .back-stripe {
    position: absolute; top: 0; bottom: 0; right: 0; width: 30px; background: var(--ink);
  }
  .back-stripe--accent { right: 30px; width: 8px; background: var(--brand-blue); }
  .back-content { position: absolute; left: 30px; top: 40px; }
  .back-mark { display: flex; align-items: center; gap: 8px; }
  .back-mark__dot { flex: none; width: 11px; height: 11px; border-radius: 50%; background: var(--ink); }
  .back-mark__name { font-weight: 700; font-size: 18px; line-height: 1; color: var(--ink); white-space: nowrap; }
  .contact { margin-top: 40px; }
  .contact__person { font-size: 19px; font-weight: 700; color: var(--brand-blue); }
  .contact__role { font-size: 12px; font-weight: 400; color: var(--ink); margin-left: 4px; }
  .contact__line { margin-top: 6px; font-size: 12.5px; color: var(--ink); }
  .contact__label { color: var(--brand-blue); }
  .contact__abn { margin-top: 6px; font-size: 12.5px; font-weight: 700; color: var(--ink); }
</style>
</head>
<body>
  <main class="sheet">
    <section class="card card--front" aria-label="Card front">
      <div class="front-mark">
        <span class="front-mark__dot"></span>
        <span class="front-mark__name">Coral Vehicle Supplies</span>
      </div>
    </section>

    <section class="card card--back" aria-label="Card back">
      <span class="back-ghost" aria-hidden="true">Coral<br>Vehicle<br>Supplies</span>
      <span class="back-stripe back-stripe--accent"></span>
      <span class="back-stripe"></span>
      <div class="back-content">
        <div class="back-mark">
          <span class="back-mark__dot"></span>
          <span class="back-mark__name">Coral Vehicle Supplies</span>
        </div>
        <div class="contact">
          <p class="contact__person">Morris Tandy<span class="contact__role">Director</span></p>
          <p class="contact__line"><span class="contact__label">Mobile :</span> 0438 271 954</p>
          <p class="contact__line"><span class="contact__label">Email :</span> mtandyo@bellwire.com.au</p>
          <p class="contact__abn">ABN number: 47 316 208 594</p>
        </div>
      </div>
    </section>
  </main>
</body>
</html>
```